Modern Yoga Studio Timetable and Flyer Design

We have a comprehensive class timetable and we are wanting to a clean modern look for our Spring timetable.

We require a double sided flyer with our class timetable included.
We would prefer an A5 size (postcard) or DL (1/3 A4).

We would like the final flyer to have.
Side A : Yoga image, logo

Fennel Stretch Hall
address: 4/71 Wexcombe Lane, Pelharton
website: fennelstretch.com.au
mobile: 0471 296 814

Side B: Clear easy to read timetable with a break down of class types and website.

We would also like to have a copy of the timetable itself as a separate jpg or pdf for use on our website to download.

Thank you.
Yours kindly,
Nell

I have attached a sample of another timetable of which I like the look and feel of, however this is just a guide. I've also attached our 'new' schedule in WORD plus uploaded our last design of the front.
Updates

Target Market(s)

Women aged 30-45

Industry/Entity Type

Health And Wellness

Font styles to use
Other font styles liked:
• Brandon Grotesque, Jenna Sue

Colors
6c459b
33a6d7
ffffff

Requirements
Must have
• A definitive colour to decipher between different class types on our timetable. Where each colour represents a different class type. Colours and layouts similar to our website design, see www.fennelstretch.com.au
Nice to have
• I've included a design of another studio whose timetable design I like. One of our own yoga images instead of a stock image.
Should not have
• No dark gridlines between the cells/boxes in the timetables. Please don't use stock yoga images.

```html
<!DOCTYPE html>
<html lang="en">
<head>
<meta charset="utf-8">
<title>Fennel Stretch Hall – Spring Flyer</title>
<link href="https://fonts.googleapis.com/css2?family=Caveat:wght@400;600&family=Marcellus&display=swap" rel="stylesheet">
<style>
  :root {
    --backdrop: #7d95c6;
    --violet: #6c459b;
    --violet-deep: #3f2f86;
    --sky: #33a6d7;
    --white: #ffffff;
    --lilac: #c8a2cf;
    --lilac-soft: #e6d3ea;
    --rose: #c0739f;
    --navy: #2e3a8c;
    --plum: #5a2a6a;
    --magenta: #8a2a91;
    --pale-blue: #cfc8e4;
    --pale-grey: #dccfe2;
    --cyan-soft: #9fdcea;
    --teal-soft: #b4dcdc;
  }
  * { box-sizing: border-box; margin: 0; padding: 0; }
  html, body { width: 848px; height: 1200px; overflow: hidden; }
  body { background: var(--backdrop); font-family: "Marcellus", serif; position: relative; }

  .flyer { position: absolute; left: 59px; width: 731px; height: 515px; overflow: hidden; }
  .flyer--front { top: 46px;
    background: linear-gradient(100deg, #8e6bb5 0%, #b58fca 35%, #d4b4dc 70%, #f3e9f4 100%); }
  .flyer--back { top: 583px;
    background: linear-gradient(180deg, #a27cc0 0%, #c79ed0 40%, #d7b2d8 80%, #ecd9ee 100%); }

  /* front */
  .headline { position: absolute; top: 24px; left: 0; width: 100%; text-align: center; white-space: nowrap;
    font-family: "Caveat", cursive; font-weight: 400; font-size: 56px; color: var(--violet-deep); line-height: 1; }
  .tagline { position: absolute; top: 112px; left: 0; width: 100%; text-align: center; white-space: nowrap;
    font-size: 14px; color: var(--violet-deep); }
  .photo { position: absolute; left: 18px; top: 146px; width: 436px; height: 272px; border-radius: 50% 50% 40% 40% / 60% 60% 30% 30%;
    background: radial-gradient(ellipse at 50% 55%, #f4dcea 0%, #e2c0df 45%, rgba(214,178,220,0) 75%); }
  .ornament { position: absolute; left: 422px; top: 150px; width: 172px; height: 130px; border-radius: 50%;
    background: radial-gradient(circle, rgba(150,110,170,0.35) 0%, rgba(150,110,170,0.12) 60%, rgba(150,110,170,0) 75%); }
  .swoosh { position: absolute; left: 0; top: 0; width: 731px; height: 515px; }
  .studio-name { position: absolute; left: 74px; top: 424px; font-size: 22px; letter-spacing: 3px; color: var(--violet-deep); }
  .join { position: absolute; right: 22px; top: 270px; text-align: right; font-family: "Caveat", cursive; color: var(--white); line-height: 0.85; }
  .join .big { display: block; font-size: 66px; }
  .join .small { display: block; font-size: 44px; }
  .contact { position: absolute; right: 16px; text-align: right; color: var(--white); white-space: nowrap; }
  .contact--phone { top: 384px; font-size: 32px; letter-spacing: 1px; }
  .contact--email { top: 426px; font-size: 16px; }
  .contact--address { top: 459px; font-size: 9px; letter-spacing: 0.3px; }
  .contact--web { top: 476px; font-size: 21px; color: var(--violet); }

  /* back */
  .tt-title { position: absolute; top: 6px; left: 0; width: 100%; text-align: center; white-space: nowrap;
    font-family: "Caveat", cursive; font-weight: 600; font-size: 58px; color: var(--white); line-height: 1; }
  .day-band { position: absolute; top: 83px; left: 0; width: 100%; height: 16px; background: var(--violet); }
  .day { position: absolute; top: 0; width: 76px; text-align: center; font-size: 11px; line-height: 16px; color: var(--white); }
  .time { position: absolute; left: 70px; width: 44px; text-align: right; font-size: 8.5px; color: #b04d8c; }
  .lotus { position: absolute; right: 12px; bottom: 30px; width: 220px; height: 140px; border-radius: 50% 50% 30% 30%;
    background: radial-gradient(ellipse at 50% 60%, rgba(200,140,200,0.55) 0%, rgba(230,200,235,0.35) 50%, rgba(230,200,235,0) 75%); }
  .cls { position: absolute; width: 76px; height: 29px; display: flex; align-items: center; justify-content: center;
    text-align: center; font-size: 9.5px; line-height: 1.2; color: var(--white); white-space: nowrap; }
  .cls--vinyasa { background: var(--rose); }
  .cls--slow { background: var(--violet); }
  .cls--rise { background: #c8b4d6; }
  .cls--yin { background: var(--lilac-soft); }
  .cls--pregnancy { background: var(--pale-grey); }
  .cls--mumbaby { background: var(--pale-blue); }
  .cls--kids-older { background: var(--sky); }
  .cls--kids-younger { background: var(--navy); }
  .cls--teens { background: var(--cyan-soft); }
  .cls--restore { background: var(--plum); justify-content: flex-start; text-align: left; padding-left: 10px; }
  .cls--yin-restore { background: var(--teal-soft); }
  .cls--wellness { background: var(--magenta); }
  .footer-band { position: absolute; left: 0; bottom: 0; width: 100%; height: 21px; background: var(--violet);
    text-align: center; font-size: 11px; line-height: 21px; color: var(--white); }
</style>
</head>
<body>

<section class="flyer flyer--front">
  <h1 class="headline">All levels Yoga classes in Pelharton</h1>
  <p class="tagline">Fennel Stretch Hall, a boutique yoga studio located in Perth's leafy northern suburb of Pelharton</p>
  <div class="ornament" role="img" aria-label="Faint mandala ornament"></div>
  <div class="photo" role="img" aria-label="Photo of a woman meditating cross-legged in front of large lotus petals"></div>
  <svg class="swoosh" viewBox="0 0 731 515" aria-hidden="true">
    <path d="M250 515 C 420 380, 560 250, 731 220 L731 515 Z" fill="#c58fc4" opacity="0.85"/>
    <path d="M250 515 C 420 380, 560 250, 731 220" fill="none" stroke="#f6eaf5" stroke-width="3"/>
  </svg>
  <p class="studio-name">Fennel Stretch Hall</p>
  <p class="join"><span class="big">Join</span><span class="small">a Studio Class</span></p>
  <p class="contact contact--phone">0471 296 814</p>
  <p class="contact contact--email">hello@fennelstretch.com.au</p>
  <p class="contact contact--address">Marlow Shopping Ctr - 4/71 WEXCOMBE LANE - PELHARTON WA 6091</p>
  <p class="contact contact--web">www.fennelstretch.com.au</p>
</section>

<section class="flyer flyer--back">
  <h2 class="tt-title">Fennel Stretch Spring Timetable</h2>
  <div class="day-band">
    <span class="day" style="left:132px">MONDAY</span>
    <span class="day" style="left:208px">TUESDAY</span>
    <span class="day" style="left:284px">WEDNESDAY</span>
    <span class="day" style="left:360px">THURSDAY</span>
    <span class="day" style="left:436px">FRIDAY</span>
    <span class="day" style="left:514px">SATURDAY</span>
    <span class="day" style="left:590px">SUNDAY</span>
  </div>

  <div class="lotus" role="img" aria-label="Soft lotus flower decoration"></div>

  <span class="time" style="top:119px">545AM</span>
  <span class="time" style="top:146px">900AM</span>
  <span class="time" style="top:174px">915AM</span>
  <span class="time" style="top:202px">930AM</span>
  <span class="time" style="top:229px">1030AM</span>
  <span class="time" style="top:257px">11AM</span>
  <span class="time" style="top:285px">1215PM</span>
  <span class="time" style="top:313px">4PM</span>
  <span class="time" style="top:341px">445PM</span>
  <span class="time" style="top:369px">500PM</span>
  <span class="time" style="top:396px">600PM</span>
  <span class="time" style="top:424px">615PM</span>
  <span class="time" style="top:451px">730PM</span>

  <div class="cls cls--rise" style="left:208px;top:110px">RISE + SHINE*</div>
  <div class="cls cls--rise" style="left:360px;top:110px">RISE + SHINE*</div>
  <div class="cls cls--vinyasa" style="left:514px;top:134px">VINYASA FLOW</div>
  <div class="cls cls--yin" style="left:590px;top:166px">YIN</div>
  <div class="cls cls--vinyasa" style="left:208px;top:166px">VINYASA FLOW</div>
  <div class="cls cls--slow" style="left:132px;top:194px">SLOW FLOW</div>
  <div class="cls cls--vinyasa" style="left:360px;top:192px">VINYASA FLOW</div>
  <div class="cls cls--pregnancy" style="left:514px;top:220px">PREGNANCY*</div>
  <div class="cls cls--mumbaby" style="left:208px;top:246px">MUM + BABY*</div>
  <div class="cls cls--mumbaby" style="left:360px;top:240px">MUM + BABY*</div>
  <div class="cls cls--pregnancy" style="left:360px;top:268px">PREGNANCY*</div>
  <div class="cls cls--kids-older" style="left:284px;top:297px">KIDS 8-12*</div>
  <div class="cls cls--kids-younger" style="left:360px;top:297px">KIDS 5- 7*</div>
  <div class="cls cls--vinyasa" style="left:514px;top:297px">VINYASA FLOW</div>
  <div class="cls cls--teens" style="left:284px;top:326px">TEENS 12-16*</div>
  <div class="cls cls--teens" style="left:360px;top:360px">TEENS 12-16*</div>
  <div class="cls cls--pregnancy" style="left:132px;top:390px">PREGNANCY*</div>
  <div class="cls cls--vinyasa" style="left:208px;top:390px">VINYASA FLOW</div>
  <div class="cls cls--slow" style="left:284px;top:390px">SLOW FLOW</div>
  <div class="cls cls--pregnancy" style="left:360px;top:390px">PREGNANCY*</div>
  <div class="cls cls--restore" style="left:436px;top:390px">FLOW +<br>RESTORE</div>
  <div class="cls cls--vinyasa" style="left:132px;top:446px">VINYASA FLOW</div>
  <div class="cls cls--pregnancy" style="left:208px;top:446px">PREGNANCY*</div>
  <div class="cls cls--yin-restore" style="left:284px;top:446px">YIN + RESTORE</div>
  <div class="cls cls--wellness" style="left:360px;top:446px">WOMEN'S<br>WELLNESS*</div>

  <p class="footer-band">www.fennelstretch.com.au</p>
</section>

</body>
</html>
```